Healing stone/crystal Shopify store

Hi - I'm creating a new site to sell healing crystals/stones.Name for the shop is MoonpetalHaven. Site helps people to choose best crystals for them .Shop should have blog aswell.The site should be informative and attractive. Stones we sell Opalite,Green Aventurine,Watermelon Crystal,Rose Quartz Stone,Tiger Eye Stone. Must be Shopify. No content yet, you can fill neccessary fields Lorea Ipsum and if you have some good idea you can put it there
Updates

Designs look the same

Target Market(s)

Woman, English speaking countries.

Industry/Entity Type

Shop

Number of Pages Required

1 page

Colors

Designer to choose colors to be used in the design.

Requirements
Must have
• Blog
Nice to have
• High quality pictures to look site attractive.

```html
<!DOCTYPE html>
<html lang="en">
<head>
<meta charset="utf-8">
<title>MoonpetalHaven – Healing Crystals</title>
<link rel="stylesheet" href="https://fonts.googleapis.com/css2?family=Lato:wght@300;400;700;900&display=swap">
<style>
:root{
  --ink:#111;--page:#000;--yellow:#f7dc00;--navy:#1c2347;--grey:#e6e6e6;--light:#f4f4f4;
  --foot:#1b1b1b;--muted:#777;--white:#fff;--orange:#e07a1e;
}
*{box-sizing:border-box;margin:0;padding:0}
html,body{width:1200px;height:1200px;overflow:hidden;background:var(--page);font-family:'Lato',sans-serif;color:var(--ink)}
.site{position:absolute;left:441px;top:0;width:398px;height:1500px;transform:scale(.8);transform-origin:0 0;background:var(--white);overflow:hidden}
.abs{position:absolute}
.fill{position:absolute}
/* hero */
.hero{left:0;top:0;width:398px;height:201px;background:radial-gradient(circle at 300px 110px,#c9cde0 0,#6f7596 30%,#3b4266 70%,#2b3152 100%)}
.topbar{left:0;top:0;width:398px;height:23px;background:rgba(20,24,45,.55)}
.logo{left:21px;top:6px;font-size:9.5px;line-height:12px;color:var(--white);font-weight:400;white-space:nowrap}
.logo b{color:var(--yellow);font-weight:400}
.nav{right:20px;top:9px;display:flex;gap:9px;font-size:4px;line-height:5px;color:var(--white)}
.nav .on{color:var(--yellow);border-bottom:1px solid var(--yellow);padding-bottom:2px}
.hero-title{left:22px;top:76px;font-size:11.5px;line-height:14px;font-weight:700;color:var(--white);white-space:nowrap}
.hero-sub{left:22px;top:94px;width:180px;font-size:6.5px;font-weight:300;color:#e8e8f0;line-height:1.4}
.btn-shop{left:21px;top:123px;width:63px;height:20px;border:1px solid var(--yellow);color:var(--yellow);font-size:7px;font-weight:700;display:flex;align-items:center;justify-content:center}
.chev{left:193px;top:177px}
.catbar{left:0;top:201px;width:398px;height:17px;background:var(--yellow);display:flex;justify-content:center;gap:20px;align-items:center;font-size:4px;color:#333}
/* products */
.card-img{background:#fff;border:1px solid #eee}
.meta{font-size:3px;color:#666;line-height:1.6}
.meta b{color:#222;font-weight:700}
.price{font-size:4.5px;font-weight:700;color:#222}
/* about */
.about{left:0;top:488px;width:195px;height:174px;background:var(--navy);color:var(--white);text-align:center}
.about h2{font-size:15px;font-weight:300;margin-top:22px}
.about p{font-size:3.6px;line-height:2.7;margin:10px 14px 0;color:#d8dbe9}
/* section titles */
.tag{left:50%;transform:translateX(-50%);background:var(--yellow);font-size:3.6px;font-weight:700;padding:1px 5px;color:#333;white-space:nowrap}
.title{left:0;width:398px;text-align:center;font-size:6.2px;font-weight:900;color:#1c2347}
.div{left:50%;transform:translateX(-50%)}
.tile{top:725px;height:101px;width:78px}
/* blog */
.blog{left:0;top:1067px;width:398px;height:183px;background:linear-gradient(90deg,#9c7b10 0,#d79d1b 35%,#d48a18 65%,#a05a0a 100%)}
.post{top:1123px;width:97px;height:94px;background:var(--white)}
.post .ph{height:47px;background:linear-gradient(180deg,#1a1a1a,#4a4a55)}
.post .pm{font-size:3px;color:#777;padding:4px 7px 0;display:flex;justify-content:space-between}
.post h4{font-size:4.2px;font-weight:700;padding:3px 7px 1px}
.post p{font-size:3.2px;color:#666;padding:0 7px;line-height:1.5}
.post .rm{font-size:3px;color:#999;padding:4px 7px}
/* newsletter */
.news{left:0;top:1250px;width:398px;height:118px;background:var(--light)}
.news-tag{left:108px;top:1276px;background:var(--yellow);font-size:3.6px;font-weight:700;padding:1px 5px;color:#333}
/* footer */
.foot{left:0;top:1368px;width:398px;height:132px;background:var(--foot);color:#aaa;font-size:3.5px}
.fcol{line-height:2.8}
.fcol h5{font-size:4px;font-weight:400;color:#ddd}
.get{left:268px;width:84px;border-bottom:1px solid #444;height:13px;display:flex;align-items:center;gap:4px}
.sq{width:8px;height:8px;border:1px solid var(--orange);top:1455px}
</style>
</head>
<body>
<div class="site">
  <!-- hero -->
  <div class="fill hero" role="img" aria-label="Photo of clear crystal spheres with soft bokeh lights in blue tones"></div>
  <div class="abs topbar"></div>
  <div class="abs logo">Moonpetal<b>Haven</b></div>
  <nav class="abs nav"><span class="on">Home</span><span>About Us</span><span>Blog</span><span>Contact Us</span><span>Login</span></nav>
  <h1 class="abs hero-title">Lorem ipsum dolor sit amet consectetur</h1>
  <p class="abs hero-sub">Sed tellus nisl, aliquam ut sem in, semper dignissim justo. Vestibulum et</p>
  <div class="abs btn-shop">Shop Now</div>
  <svg class="abs chev" width="12" height="10" viewBox="0 0 12 10"><path d="M2 1l4 3 4-3M2 5l4 3 4-3" fill="none" stroke="#f7dc00" stroke-width="1.2"/></svg>
  <div class="abs catbar"><span>Products</span><span>Jewelry</span><span>Selenite</span><span>Shungite</span><span>Accessories</span></div>

  <!-- featured products -->
  <div class="fill card-img" style="left:52px;top:241px;width:68px;height:87px;background:linear-gradient(160deg,#fff 20%,#f3c4cc 55%,#fff 85%)" role="img" aria-label="Rose quartz carved angel figure"></div>
  <div class="abs meta" style="left:52px;top:331px">Lorem ipsum dolor sit amet<br><b>SED TELLUS NISL ALIQUAM</b></div><div class="abs price" style="left:108px;top:331px">$ 470</div>
  <div class="fill card-img" style="left:52px;top:355px;width:68px;height:87px;background:radial-gradient(circle,#5d4a6e 0,#8a7a98 35%,#fff 70%)" role="img" aria-label="Amethyst angel figures arranged in a circle"></div>
  <div class="abs meta" style="left:52px;top:445px">Lorem ipsum dolor sit amet<br><b>SED TELLUS NISL ALIQUAM</b></div><div class="abs price" style="left:108px;top:445px">$ 470</div>
  <div class="fill" style="left:128px;top:241px;width:143px;height:218px;background:linear-gradient(135deg,#e9cc58,#f6e6a3 50%,#d9b845)" role="img" aria-label="Yellow crystal flower brooch with gold setting"></div>
  <div class="fill card-img" style="left:278px;top:241px;width:69px;height:87px;background:radial-gradient(ellipse at 50% 50%,#d9485e 0,#e8879a 25%,#fff 55%)" role="img" aria-label="Strawberry quartz carved elephant"></div>
  <div class="abs meta" style="left:278px;top:331px">Lorem ipsum dolor sit amet<br><b>SED TELLUS NISL ALIQUAM</b></div><div class="abs price" style="left:335px;top:331px">$ 470</div>
  <div class="fill card-img" style="left:278px;top:355px;width:69px;height:87px;background:radial-gradient(circle,#7a4e22 0,#b5844a 30%,#fff 65%)" role="img" aria-label="Tiger eye carved angel figures"></div>
  <div class="abs meta" style="left:278px;top:445px">Lorem ipsum dolor sit amet<br><b>SED TELLUS NISL ALIQUAM</b></div><div class="abs price" style="left:335px;top:445px">$ 470</div>

  <!-- about -->
  <div class="abs about">
    <h2>About Us</h2>
    <p>Lorem ipsum dolor sit amet, consectetur adipiscing elit. Sed tellus nisl, aliquam ut sem in, semper dignissim justo. Vestibulum et aliquam arcu, eu lobortis leo. Donec sodales, turpis at pretium porttitor, justo sem sodales est, sed ullamcorper ipsum diam quis est. Vestibulum non est nec nulla finibus aliquam at vitae mauris. Vestibulum feugiat tellus tellus, sed aliquam odio egestas nec. Suspendisse efficitur rutrum orci sit amet molestie. Pellentesque mollis eros in accumsan sagittis. Class aptent taciti sociosqu ad litora torquent per conubia nostra. Vestibulum feugiat congue odio. Etiam eu lacus arcu. Praesent id lacus eget elit tincidunt malesuada at vel nisl. In hac habitasse platea dictumst. Integer at sapien pharetra, mollis eros vitae, fringilla ante. Praesent auctor vel metus quis pharetra. Sed suscipit ultricies tortor at dignissim nisi.</p>
  </div>
  <div class="fill" style="left:195px;top:488px;width:203px;height:174px;background:linear-gradient(160deg,#f2eee6 0,#c9bba6 40%,#b7a78e 100%)" role="img" aria-label="White lotus flower with polished tumbled healing stones on linen"></div>

  <!-- shop by collection -->
  <div class="fill" style="left:0;top:662px;width:398px;height:199px;background:var(--grey)"></div>
  <div class="abs tag" style="top:687px">New Trend</div>
  <div class="abs title" style="top:698px">SHOP BY COLLECTION</div>
  <svg class="abs div" style="top:708px" width="40" height="6" viewBox="0 0 40 6"><path d="M0 3h15M25 3h15" stroke="#1c2347" stroke-width=".6"/><path d="M17 2l3 3 3-3-1-1h-4z" fill="none" stroke="#1c2347" stroke-width=".5"/></svg>
  <div class="fill tile" style="left:0;background:radial-gradient(circle,#2d3368 0,#6a6f9a 35%,#fff 68%)" role="img" aria-label="Sodalite angel figures"></div>
  <div class="fill tile" style="left:80px;background:radial-gradient(circle,#4a3b55 0,#8e7f9a 35%,#fff 68%)" role="img" aria-label="Amethyst angel figures in a circle"></div>
  <div class="fill tile" style="left:160px;background:radial-gradient(circle,#4a2d14 0,#8f6a42 35%,#fff 68%)" role="img" aria-label="Tiger eye elephant carvings"></div>
  <div class="fill tile" style="left:240px;background:radial-gradient(circle,#161c55 0,#4a5190 30%,#fff 62%)" role="img" aria-label="Blue goldstone angel figure"></div>
  <div class="fill tile" style="left:320px;width:78px;background:radial-gradient(circle,#5e9e74 0,#a6d4b3 35%,#fff 68%)" role="img" aria-label="Green aventurine angel figures"></div>

  <!-- shop by women -->
  <div class="abs tag" style="top:879px">New Trend</div>
  <div class="abs title" style="top:894px">SHOP BY WOMENS</div>
  <svg class="abs div" style="top:904px" width="40" height="6" viewBox="0 0 40 6"><path d="M0 3h15M25 3h15" stroke="#1c2347" stroke-width=".6"/><path d="M17 2l3 3 3-3-1-1h-4z" fill="none" stroke="#1c2347" stroke-width=".5"/></svg>
  <div class="abs" style="left:0;top:919px;width:398px;display:flex;justify-content:center;gap:11px;font-size:4px;color:#333"><span>Rings</span><span>Necklace</span><span>Earings</span><span>Bangles</span><span>Chain</span></div>
  <div class="fill" style="left:52px;top:939px;width:68px;height:86px;background:radial-gradient(circle at 50% 70%,#1d2bb0 0,#171a2c 40%,#0d0d10 80%)" role="img" aria-label="Gold necklace with blue crystal pendant"></div>
  <div class="fill" style="left:128px;top:939px;width:67px;height:86px;background:radial-gradient(circle at 45% 40%,#1aa58a 0,#c69a58 30%,#0d0d0d 70%)" role="img" aria-label="Gold ring with green crystal stone"></div>
  <div class="fill" style="left:203px;top:939px;width:68px;height:86px;background:radial-gradient(circle at 50% 75%,#2aa6e0 0,#13324a 40%,#0a0a0a 80%)" role="img" aria-label="Blue crystal point pendants on chains"></div>
  <div class="fill" style="left:278px;top:939px;width:69px;height:86px;background:radial-gradient(circle at 50% 60%,#4a40c8 0,#1a1c3c 40%,#0a0a0e 80%)" role="img" aria-label="Glowing moon pendant necklaces"></div>
  <div class="abs meta" style="left:52px;top:1028px">Lorem ipsum dolor sit amet<br><b>SED TELLUS NISL ALIQUAM</b></div><div class="abs price" style="left:108px;top:1028px">$ 470</div>
  <div class="abs meta" style="left:128px;top:1028px">Lorem ipsum dolor sit amet<br><b>SED TELLUS NISL ALIQUAM</b></div><div class="abs price" style="left:184px;top:1028px">$ 470</div>
  <div class="abs meta" style="left:203px;top:1028px">Lorem ipsum dolor sit amet<br><b>SED TELLUS NISL ALIQUAM</b></div><div class="abs price" style="left:259px;top:1028px">$ 470</div>
  <div class="abs meta" style="left:278px;top:1028px">Lorem ipsum dolor sit amet<br><b>SED TELLUS NISL ALIQUAM</b></div><div class="abs price" style="left:335px;top:1028px">$ 470</div>

  <!-- blog -->
  <div class="fill blog" role="img" aria-label="Warm golden blurred crystal background"></div>
  <div class="abs tag" style="top:1089px">BLOGS</div>
  <div class="abs title" style="top:1099px;color:#fff">BLOGS POST</div>
  <svg class="abs div" style="top:1109px" width="40" height="6" viewBox="0 0 40 6"><path d="M0 3h15M25 3h15" stroke="#fff" stroke-width=".6"/><path d="M17 2l3 3 3-3-1-1h-4z" fill="none" stroke="#fff" stroke-width=".5"/></svg>
  <svg class="abs" style="left:29px;top:1158px" width="12" height="20" viewBox="0 0 12 20"><path d="M10 1L2 10l8 9" fill="none" stroke="#fff" stroke-width="1.2"/></svg>
  <svg class="abs" style="left:357px;top:1158px" width="12" height="20" viewBox="0 0 12 20"><path d="M2 1l8 9-8 9" fill="none" stroke="#fff" stroke-width="1.2"/></svg>
  <article class="abs post" style="left:49px"><div class="ph" role="img" aria-label="Clear quartz cluster on black"></div><div class="pm"><span>April 29, 2018</span><span>2 Comment</span></div><h4>Online domination</h4><p>6 Steps to building your online presence. Being found online is one of the most powerful tools we have today.</p><div class="rm">Read More</div></article>
  <article class="abs post" style="left:151px"><div class="ph" style="background:radial-gradient(circle,#6a3c8a 0,#b3a5b8 40%,#eee 70%)" role="img" aria-label="Amethyst geode slice"></div><div class="pm"><span>April 29, 2018</span><span>2 Comment</span></div><h4>Online domination</h4><p>6 Steps to building your online presence. Being found online is one of the most powerful tools we have today.</p><div class="rm">Read More</div></article>
  <article class="abs post" style="left:252px"><div class="ph" role="img" aria-label="Clear crystal points on black"></div><div class="pm"><span>April 29, 2018</span><span>2 Comment</span></div><h4>Online domination</h4><p>6 Steps to building your online presence. Being found online is one of the most powerful tools we have today.</p><div class="rm">Read More</div></article>

  <!-- newsletter -->
  <div class="fill news"></div>
  <div class="abs news-tag">Trends</div>
  <div class="abs" style="left:26px;top:1286px;width:200px;text-align:center;font-size:6.2px;font-weight:900;color:#1c2347">SIGN UP NEWSLETTER</div>
  <svg class="abs" style="left:106px;top:1296px" width="40" height="6" viewBox="0 0 40 6"><path d="M0 3h15M25 3h15" stroke="#1c2347" stroke-width=".6"/><path d="M17 2l3 3 3-3-1-1h-4z" fill="none" stroke="#1c2347" stroke-width=".5"/></svg>
  <p class="abs" style="left:50px;top:1307px;width:152px;text-align:center;font-size:3.4px;color:#666;line-height:1.6">Subscribe to our newsletters now and stay up-to-date with new collections, the latest lookbooks and exclusive offers.</p>
  <div class="abs" style="left:55px;top:1330px;width:108px;height:11px;background:#fff;border:1px solid #ddd;font-size:3px;color:#aaa;padding:3px 4px">Your Email Address</div>
  <div class="abs" style="left:163px;top:1330px;width:35px;height:11px;background:var(--navy);color:#fff;font-size:3.2px;font-weight:700;display:flex;align-items:center;justify-content:center">SUBSCRIBE</div>
  <div class="fill" style="left:245px;top:1250px;width:153px;height:118px;background:radial-gradient(ellipse at 50% 50%,#8a5a3a 0,#3c7a6a 35%,#c9442c 55%,#f4f4f4 78%)" role="img" aria-label="Polished colourful tumbled stones"></div>

  <!-- footer -->
  <footer class="abs foot">
    <div class="abs fcol" style="left:41px;top:14px"><h5>On this site</h5>Crystal Guide<br>Articles<br>Blog<br>Contact Us</div>
    <div class="abs fcol" style="left:91px;top:14px"><h5>Categories</h5>Mountain<br>Water<br>Metro<br>Ranch</div>
    <div class="abs fcol" style="left:133px;top:14px"><h5>Other Links</h5>Shipping &amp; Returns<br>RSS Syndication</div>
    <div class="abs" style="left:268px;top:16px;width:84px;text-align:center;font-size:4px;color:#ddd">Get In Touch</div>
    <div class="abs get" style="top:26px"><svg width="4" height="5" viewBox="0 0 4 5"><path d="M2 5L.4 2.4A1.8 1.8 0 1 1 3.6 2.4z" fill="#e07a1e"/></svg>18 Lumen Lane, Suite 4, USA, GA 200</div>
    <div class="abs get" style="top:39px"><svg width="4" height="4" viewBox="0 0 4 4"><path d="M.5.5h1l.5 1-.6.5a2.5 2.5 0 0 0 1 1l.5-.6 1 .5v1C2 4 0 2 .5.5z" fill="#e07a1e"/></svg>00 4100 7720</div>
    <div class="abs get" style="top:52px"><svg width="5" height="4" viewBox="0 0 5 4"><rect width="5" height="4" fill="#e07a1e"/><path d="M0 0l2.5 2L5 0" stroke="#1b1b1b" stroke-width=".5" fill="none"/></svg>hello@moonpetalhaven.com</div>
    <div class="abs get" style="top:65px;border:0"><svg width="5" height="4" viewBox="0 0 5 4"><rect y="1" width="5" height="3" fill="#e07a1e"/></svg>555 014 2288</div>
    <div class="abs" style="left:41px;top:104px;width:311px;border-top:1px solid #333"></div>
    <div class="abs" style="left:0;top:113px;width:398px;text-align:center;font-size:3px;color:#999">© 2017 Moonpetal Haven Co. All rights reserved.</div>
  </footer>
  <div class="abs sq" style="left:43px"></div>
  <div class="abs sq" style="left:55px"></div>
  <div class="abs sq" style="left:67px"></div>
</div>
</body>
</html>
```